Varelto Solutions
Stationary
Project: Varelto Solutions
Varelto Solutions - Consulting
Creative Brief
Professional
Tarik Hembrow
MD & CEO
3518, Crestmoor Plaza Falcon Bay Quarter Dubai, PO Box 672914 UAE
Tarik.Hembrow@Varelto.com
www.varelto.com
Place company logo (Varelto) on front side and product logo (Kestrel) on the back side of the card. Review our website www.varelto.com for look and feel.
Banking Business Intelligence Enterprise Risk Management Europe - Africa - Middle East - South Asia - APAC

```html
<!DOCTYPE html>
<html lang="en">
<head>
<meta charset="utf-8">
<title>Varelto Solutions – Business Card</title>
<link href="https://fonts.googleapis.com/css2?family=Exo+2:wght@800&family=Open+Sans:wght@400;600&display=swap" rel="stylesheet">
<style>
  :root {
    --navy: #1c2f7d;
    --red: #c8202f;
    --paper: #ffffff;
    --stage: #e4e4e4;
    --ink: #5a5a5a;
  }
  * { box-sizing: border-box; margin: 0; padding: 0; }
  html, body { width: 1200px; height: 895px; overflow: hidden; }
  body {
    background: var(--stage);
    font-family: "Open Sans", Arial, sans-serif;
    position: relative;
  }
  .card {
    position: absolute;
    left: 260px;
    width: 680px;
    height: 390px;
    background: var(--paper);
    box-shadow: 0 2px 8px rgba(0,0,0,.12);
    overflow: hidden;
  }
  .card--product { top: 40px; }
  .card--contact { top: 465px; }

  .brand { position: absolute; display: flex; flex-direction: column; align-items: flex-end; }
  .brand__row { display: flex; align-items: center; gap: 12px; }
  .brand__dot { border-radius: 50%; background: var(--red); flex: none; }
  .brand__name {
    font-family: "Exo 2", Arial, sans-serif;
    font-weight: 800;
    color: var(--navy);
    line-height: 1;
  }
  .brand__tagline { color: var(--red); font-size: 11px; letter-spacing: .3px; margin-top: 4px; }

  .card--product .brand { left: 50%; top: 50%; transform: translate(-50%, -50%); }
  .card--product .brand__dot { width: 62px; height: 62px; }
  .card--product .brand__name { font-size: 68px; }
  .card--product .brand__tagline { font-size: 13px; }

  .card--contact .brand { left: 36px; top: 46px; }
  .card--contact .brand__dot { width: 46px; height: 46px; }
  .card--contact .brand__name { font-size: 48px; }

  .band { position: absolute; }
  .band--red { left: 0; top: 150px; width: 232px; height: 50px; background: var(--red); }
  .band--blue {
    left: 232px; top: 204px; width: 448px; height: 46px; background: var(--navy);
    color: #fff; font-size: 14px; display: flex; align-items: center; padding-left: 28px;
    letter-spacing: .3px;
  }

  .person { position: absolute; right: 40px; top: 150px; text-align: left; }
  .person__name { color: var(--red); font-size: 17px; letter-spacing: 1px; }
  .person__title { color: var(--navy); font-size: 13px; letter-spacing: 1px; }

  .contact-list { position: absolute; list-style: none; }
  .contact-list li {
    display: flex; align-items: flex-start; gap: 9px;
    font-size: 11px; line-height: 15px; color: var(--ink); margin-bottom: 5px;
  }
  .contact-list .icon { width: 13px; height: 13px; margin-top: 1px; background: var(--navy); flex: none; }
  .contact-list--details { left: 30px; top: 212px; width: 200px; }
  .contact-list--social { left: 400px; top: 290px; }
</style>
</head>
<body>
  <section class="card card--product">
    <div class="brand">
      <div class="brand__row">
        <span class="brand__dot"></span>
        <span class="brand__name">Kestrel</span>
      </div>
      <span class="brand__tagline">Insight through shared knowledge</span>
    </div>
  </section>

  <section class="card card--contact">
    <div class="band band--red"></div>
    <div class="brand">
      <div class="brand__row">
        <span class="brand__dot"></span>
        <span class="brand__name">Varelto</span>
      </div>
      <span class="brand__tagline">Varelto Solutions</span>
    </div>

    <div class="person">
      <p class="person__name">TARIK HEMBROW</p>
      <p class="person__title">MD &amp; CEO</p>
    </div>

    <ul class="contact-list contact-list--details">
      <li><span class="icon"></span><span>3518, Crestmoor Plaza Falcon Bay Quarter<br>Dubai, PO Box 672914 UAE</span></li>
      <li><span class="icon"></span><span>Tarik.Hembrow@Varelto.com</span></li>
    </ul>

    <div class="band band--blue">www.varelto.com</div>

    <ul class="contact-list contact-list--social">
      <li><span class="icon"></span>www.varelto.com</li>
      <li><span class="icon"></span>www.chirpline.com/varelto</li>
      <li><span class="icon"></span>www.friendwall.com/varelto</li>
    </ul>
  </section>
</body>
</html>
```